The amber lantern with an elephant incorporated in the background

Target Market(s)

Real estate

Industry/Entity Type

Real Estate

Contact Information for Business Card

On back on want my name & number
In front I want the business name, "the amber lantern", below to say staging & design

Logo Text

The amber lantern

Font styles to use
Serif

Colors
000000

Requirements
Must have
• I want an elephant behind the writing in gold transperant

```html
<!DOCTYPE html>
<html lang="en">
<head>
<meta charset="utf-8">
<title>The Amber Lantern – Business Card</title>
<link href="https://fonts.googleapis.com/css2?family=Lato:wght@300;400;700&display=swap" rel="stylesheet">
<style>
  :root {
    --backdrop: #3d3e3c;
    --backdrop-edge: #2b2c2a;
    --card: #0d0d0d;
    --gold: #c2a04a;
    --gold-soft: #a88a3c;
    --gold-veil: rgba(176, 140, 62, 0.26);
    --gold-veil-light: rgba(176, 140, 62, 0.10);
  }
  * { margin: 0; padding: 0; box-sizing: border-box; }
  html, body {
    width: 1200px;
    height: 1200px;
    overflow: hidden;
  }
  body {
    background: radial-gradient(circle at 50% 45%, var(--backdrop) 0%, var(--backdrop-edge) 100%);
    font-family: "Lato", sans-serif;
    display: flex;
    flex-direction: column;
    align-items: center;
    justify-content: center;
    gap: 60px;
  }
  .card {
    position: relative;
    width: 880px;
    height: 503px;
    background: var(--card);
    box-shadow: 0 18px 40px rgba(0, 0, 0, 0.45);
    overflow: hidden;
  }

  /* Front: brand + contact */
  .brand {
    position: absolute;
    left: 80px;
    top: 250px;
  }
  .brand-row {
    display: flex;
    align-items: center;
    gap: 16px;
  }
  .brand-dot {
    width: 12px;
    height: 12px;
    border-radius: 50%;
    background: var(--gold);
  }
  .brand-name {
    color: var(--gold);
    font-weight: 400;
    font-size: 30px;
    letter-spacing: 0.14em;
    text-transform: uppercase;
    line-height: 1;
  }
  .brand-tagline {
    color: var(--gold);
    font-weight: 400;
    font-size: 14px;
    letter-spacing: 0.6em;
    text-transform: uppercase;
    margin-top: 12px;
    padding-left: 44px;
  }
  .contact {
    position: absolute;
    left: 540px;
    top: 90px;
    color: var(--gold);
  }
  .contact-name {
    font-weight: 700;
    font-size: 32px;
    line-height: 1.1;
  }
  .contact-title {
    font-weight: 400;
    font-size: 17px;
    color: var(--gold-soft);
    margin: 6px 0 0 16px;
  }
  .contact-list {
    list-style: none;
    margin: 30px 0 0 28px;
  }
  .contact-list li {
    display: flex;
    align-items: center;
    gap: 16px;
    font-size: 17px;
    margin-bottom: 16px;
  }
  .contact-icon { width: 24px; height: 20px; flex: none; }

  /* Back: name over faint gold elephant */
  .elephant-art {
    position: absolute;
    left: 120px;
    top: 20px;
    width: 720px;
    height: 470px;
    border-radius: 45% 50% 30% 35%;
    background: radial-gradient(ellipse at 60% 45%, var(--gold-veil) 0%, var(--gold-veil-light) 50%, transparent 72%);
  }
  .back-lockup {
    position: absolute;
    inset: 0;
    display: flex;
    flex-direction: column;
    align-items: center;
    justify-content: center;
    text-align: center;
  }
  .back-name {
    color: var(--gold);
    font-weight: 400;
    font-size: 48px;
    letter-spacing: 0.14em;
    text-transform: uppercase;
  }
  .back-tagline {
    color: var(--gold);
    font-weight: 400;
    font-size: 21px;
    letter-spacing: 0.7em;
    text-transform: uppercase;
    margin-top: 8px;
  }
</style>
</head>
<body>

  <section class="card card--front" aria-label="Card front">
    <div class="brand">
      <div class="brand-row">
        <span class="brand-dot"></span>
        <span class="brand-name">The Amber Lantern</span>
      </div>
      <div class="brand-tagline">Staging &amp; Design</div>
    </div>

    <div class="contact">
      <div class="contact-name">Your Name</div>
      <div class="contact-title">Job Title</div>
      <ul class="contact-list">
        <li>
          <svg class="contact-icon" viewBox="0 0 24 20" aria-hidden="true">
            <path d="M2 6 Q12 0 22 6 L20 9 L16 7 L16 5 Q12 4 8 5 L8 7 L4 9 Z" fill="#c2a04a"/>
            <rect x="5" y="10" width="14" height="9" rx="1.5" fill="#c2a04a"/>
            <circle cx="12" cy="14.5" r="2.4" fill="#0d0d0d"/>
          </svg>
          <span>000 000 0000</span>
        </li>
        <li>
          <svg class="contact-icon" viewBox="0 0 24 20" aria-hidden="true">
            <rect x="2" y="3" width="20" height="14" rx="1" fill="#c2a04a"/>
            <path d="M2 3 L12 11 L22 3" fill="none" stroke="#0d0d0d" stroke-width="1.5"/>
          </svg>
          <span>hello@amberlantern.com</span>
        </li>
      </ul>
    </div>
  </section>

  <section class="card card--back" aria-label="Card back">
    <div class="elephant-art" role="img" aria-label="Large transparent gold line drawing of an elephant behind the name"></div>
    <div class="back-lockup">
      <div class="back-name">The Amber Lantern</div>
      <div class="back-tagline">Staging &amp; Design</div>
    </div>
  </section>

</body>
</html>
```